Tri-fold flyer for Managed Services IT company

We need a tri-fold flyer design for our Managed Services IT company. Our website is here: https://pelicanfjordit.net. While we don't have to match our website we do want to incorporate the logo in the flyer. We would like a flyer that is *very* easy and quick to read/skim over and convey our message. Something like these:

https://www.artkestrel.com/design/58203917

https://47sketchyard.com/postcard-flyer-design/contests/create-lead-generating-flyer-postcard-managed-services-company-815243

http://www.marbleoaksystems.com/managed-services-no-cost-one-month/

Target Market(s)

Business to business IT services

Industry/Entity Type

It Service

Font styles to use
Serif
Sans Serif

Requirements
Must have
• *very* easy and quick to read/skim over and convey our message
Should not have
• verbose, lots of text

```html
<!DOCTYPE html>
<html lang="en">
<head>
<meta charset="utf-8">
<title>Managed IT Services – Tri-fold Inside Spread</title>
<link rel="stylesheet" href="https://fonts.googleapis.com/css2?family=Anton&family=Open+Sans:wght@400;600&display=swap">
<style>
  :root {
    --page-bg: #8fc6e6;
    --sheet-dark: #2b2c2e;
    --sheet-mid: #34373b;
    --heading-blue: #1f62c9;
    --body-text: #ececec;
    --fold-line: rgba(0,0,0,0.35);
    --gear-grey: #c9cbcd;
    --ring-blue: #1d5fc2;
  }
  * { box-sizing: border-box; margin: 0; padding: 0; }
  html, body { width: 1200px; height: 900px; overflow: hidden; background: var(--page-bg); }
  body { position: relative; font-family: "Open Sans", Arial, sans-serif; color: var(--body-text); }

  .flyer {
    position: absolute; left: 20px; top: 39px; width: 1160px; height: 822px;
    overflow: hidden; background: var(--sheet-dark);
  }
  .flyer__backdrop {
    position: absolute; inset: 0;
    background:
      radial-gradient(ellipse at 55% 45%, rgba(70,90,110,0.45), transparent 60%),
      linear-gradient(180deg, #2e3034 0%, #35383d 50%, #242527 100%);
  }
  .panel { position: absolute; top: 0; height: 100%; width: 386px; }
  .panel--left { left: 0; }
  .panel--center { left: 386px; border-left: 1px solid var(--fold-line); }
  .panel--right { left: 772px; border-left: 1px solid var(--fold-line); }

  .section-title {
    position: absolute; font-family: "Anton", Impact, sans-serif; font-weight: 400;
    color: var(--heading-blue); font-size: 27px; letter-spacing: 1.5px; line-height: 1.3;
    text-transform: uppercase;
  }
  .section-title--mixed { text-transform: none; letter-spacing: 2px; line-height: 1.3; }

  .service-list { position: absolute; list-style: none; }
  .service-list li {
    position: relative; padding-left: 26px; font-size: 13.5px; letter-spacing: 0.6px;
  }
  .service-list li::before {
    content: ""; position: absolute; left: 4px; top: 3px; width: 6px; height: 12px;
    border: solid #fff; border-width: 0 3px 3px 0; transform: rotate(40deg);
  }
  .service-list li.no-tick::before { display: none; }

  .service-list--security li { line-height: 29.7px; font-size: 13px; }
  .service-list--media li { line-height: 26.5px; font-size: 14px; }
  .service-list--managed li { line-height: 32.4px; font-size: 14px; }
  .service-list--cloud li { line-height: 26.6px; font-size: 14px; }
  .service-list--data li, .service-list--hardware li { line-height: 26.9px; font-size: 14.5px; }

  .gear-badge {
    position: absolute; left: 2px; top: 543px; width: 260px; height: 260px;
    border-radius: 50%; border: 5px solid var(--ring-blue);
    background: radial-gradient(circle at 45% 45%, #d8d9db, #b5b7ba 70%, #a4a6a9);
  }

  .glossary-title { position: absolute; left: 54px; top: 574px; font-size: 17px; font-weight: 600; letter-spacing: 0.6px; }
  .advisor-photo {
    position: absolute; left: 53px; top: 622px; width: 78px; height: 78px; border-radius: 50%;
    border: 3px solid #fff; background: linear-gradient(180deg, #e6e9ee, #5a6470);
  }
  .glossary-intro {
    position: absolute; left: 164px; top: 623px; width: 200px; font-size: 11.5px; line-height: 18px; letter-spacing: 0.3px;
  }
  .glossary-body {
    position: absolute; left: 54px; top: 705px; width: 309px; font-size: 11.5px; line-height: 18px;
    letter-spacing: 0.3px; text-align: justify;
  }
</style>
</head>
<body>
  <main class="flyer">
    <div class="flyer__backdrop" role="img" aria-label="Dark, blurred photo of monitors showing lines of code"></div>

    <section class="panel panel--left">
      <h2 class="section-title" style="left:46px; top:28px;">Security Services</h2>
      <ul class="service-list service-list--security" style="left:34px; top:80px;">
        <li>Network Security</li>
        <li>Unified Threat Management</li>
        <li>Content Filtering</li>
        <li>Spam Protection</li>
        <li class="no-tick">Security Cameras</li>
        <li>VANTOR Security Solutions</li>
        <li>Email Encryption</li>
        <li>Norvik-Certified Solutions</li>
        <li>Fully Hosted Security as a<br>Service</li>
      </ul>
      <h2 class="section-title section-title--mixed" style="left:40px; top:383px;">Media &amp; Internet<br>Services</h2>
      <ul class="service-list service-list--media" style="left:38px; top:463px;">
        <li>Website Design</li>
        <li>SiteMark ID for Websites</li>
      </ul>
      <div class="gear-badge" role="img" aria-label="Illustration of interlocking grey gears"></div>
    </section>

    <section class="panel panel--center">
      <h2 class="section-title" style="left:58px; top:28px;">Managed IT Services</h2>
      <ul class="service-list service-list--managed" style="left:50px; top:80px;">
        <li>Outsourcing your IT</li>
        <li>IT Consulting</li>
        <li>Comprehensive IT Support</li>
        <li>Remote Monitoring &amp;<br>Maintenance</li>
        <li>IT Vendor Management</li>
        <li>Co-Managed IT</li>
        <li>Stratavirt</li>
        <li>24/7 Help Desk</li>
        <li>Lumeric HyperLayer</li>
        <li>Desktop Monitoring and<br>Management</li>
      </ul>
      <h2 class="section-title" style="left:58px; top:480px;">Cloud Computing<br>Services</h2>
      <ul class="service-list service-list--cloud" style="left:50px; top:564px;">
        <li>Cloud IT Solutions</li>
        <li>Hosted Lumeric Mailhub</li>
        <li>Hosted Server</li>
        <li>Hosted Desktop</li>
        <li>Hardware Virtualization</li>
        <li>Cloud Backup &amp; File Sharing</li>
        <li>Boxhaven Cloud Storage</li>
        <li>Lumeric Skyfield</li>
        <li>Cloud Hosted VoIP</li>
      </ul>
    </section>

    <section class="panel panel--right">
      <h2 class="section-title" style="left:55px; top:25px;">Data Services</h2>
      <ul class="service-list service-list--data" style="left:43px; top:75px;">
        <li>Business Continuity</li>
        <li>Data Retrieval</li>
      </ul>
      <h2 class="section-title" style="left:55px; top:150px;">Hardware Services</h2>
      <ul class="service-list service-list--hardware" style="left:43px; top:203px;">
        <li>Hardware as a Service</li>
        <li>Computer Repair</li>
        <li>Cabling and Wiring</li>
        <li>Wireless Services</li>
        <li>High-Speed Internet Consulting</li>
        <li>Kestra Official Dealer</li>
        <li>Printer Management</li>
        <li>Official Dalbrook Dealer</li>
        <li>Quince Computer Repair</li>
        <li>Velmora Official Reseller</li>
        <li>Office Relocation Services</li>
      </ul>
      <h2 class="section-title" style="left:52px; top:522px;">Why You Need Us</h2>
      <p class="glossary-title">IT Threat Glossary</p>
      <div class="advisor-photo" role="img" aria-label="Portrait photo of an IT consultant in a suit"></div>
      <p class="glossary-intro">The Internet can be a dangerous place, especially now that hackers are taking advantage of advanced tools and threats.</p>
      <p class="glossary-body">New types of malware, ransomware, and viruses are being created every day, for the express purpose of seeing your organization fail.</p>
    </section>
  </main>
</body>
</html>
```